Non-profit sports organization needs templates for Word and InDesign

"Pelo Minis" is a non-profit organization in Winterthur, which supports the recruitment of young talent by the handball clubs in Winterthur. Every year we run several camps, a tournament for schoolchildren and several handball lessons at school.
During these activities there are always written information. So far we have not given much thought to the design. But since we think that a professional design will also lead to more interaction, we now turn to you as a designer.

For the communication with partners, sponsors, patrons, etc. we need a uniform appearance. Since different departments are currently working with different programs, we need a template for letters and documentation for Word and InDesign.

We will need the documentation template for project descriptions, information, etc.
The letter templates are needed to contact sponsors, authorities, patrons, etc.

Both the letter template and the documentation template should look modern. The design should be based on the existing flyers. Otherwise we have no other requirements so far.

Homepage: www.pelo-minis.ch

Target Market(s)

Letters, documentation or information to authorities, sponsors, associations, patrons, members, participants, etc.

Requirements
Must have
• In addition to the design, the templates should also contain a concept for titles, paragraphs, lists, etc. (colors / fonts / ...)

Word and Indesign templates

```html
<!DOCTYPE html>
<html lang="en">
<head>
<meta charset="utf-8">
<title>Pelo Minis – Sponsorship Letter</title>
<link rel="stylesheet" href="https://fonts.googleapis.com/css2?family=Montserrat:wght@400;700;800&display=swap">
<style>
  :root {
    --red: #e8312f;
    --navy: #1f2a5c;
    --blue: #2d9be0;
    --sky: #7cc6ef;
    --ink: #2b2b2b;
    --paper: #ffffff;
  }
  * { margin: 0; padding: 0; box-sizing: border-box; }
  html, body { width: 849px; height: 1200px; overflow: hidden; background: var(--paper); }
  body { font-family: "Montserrat", Arial, sans-serif; color: var(--ink); }
  .page { position: relative; width: 849px; height: 1200px; overflow: hidden; background: var(--paper); }

  .top-bands, .bottom-bands { position: absolute; left: 0; width: 849px; }
  .top-bands { top: 0; height: 130px; }
  .bottom-bands { bottom: 0; height: 90px; }

  .brand {
    position: absolute; top: 132px; left: 575px;
    display: flex; align-items: center; gap: 12px;
  }
  .brand-dot { width: 46px; height: 46px; border-radius: 50%; background: var(--blue); }
  .brand-name { font-weight: 800; font-size: 30px; color: var(--red); letter-spacing: 0.5px; }

  .margin-rule {
    position: absolute; left: 620px; top: 215px; width: 1.5px; height: 905px;
    background: var(--sky);
  }

  .letter { position: absolute; left: 80px; top: 226px; width: 522px; }
  .letter-title { font-weight: 800; font-size: 17px; letter-spacing: 0.3px; color: #111; margin-bottom: 48px; }
  .letter p { font-size: 15px; line-height: 22px; margin-bottom: 24px; }
  .letter .signature { margin-top: 6px; margin-bottom: 50px; }

  .social {
    position: absolute; left: 78px; top: 1135px;
    display: flex; align-items: center; gap: 6px;
  }
  .social-dot { width: 24px; height: 24px; border-radius: 50%; background: var(--blue); }
  .social-handle { font-size: 10px; color: var(--navy); margin-left: 4px; }

  .web-address {
    position: absolute; right: 34px; bottom: 16px;
    font-size: 12px; font-weight: 700; line-height: 14px; color: var(--paper);
    transform: rotate(-8deg); transform-origin: right center;
  }
</style>
</head>
<body>
<div class="page">
  <svg class="top-bands" viewBox="0 0 849 130" aria-hidden="true">
    <polygon points="0,45 430,0 520,0 0,88" fill="var(--red)"/>
    <polygon points="0,96 700,18 700,30 0,110" fill="var(--navy)"/>
    <polygon points="180,96 849,25 849,35 180,104" fill="var(--sky)"/>
  </svg>

  <div class="brand">
    <span class="brand-dot"></span>
    <span class="brand-name">Pelo Minis</span>
  </div>

  <div class="margin-rule"></div>

  <main class="letter">
    <h1 class="letter-title">SPONSORSHIP LETTER</h1>
    <p>[DATE]</p>
    <p>[RECIPIENT NAME],</p>
    <p>[YOUR COMPANY NAME] is an organization dedicated to [DETAIL]. However, the success of the organization is largely dependent upon the product and financial support that we get from corporations and individual sponsors.</p>
    <p>We are therefore asking you to become one of this year’s sponsors. Your company can largely benefit from the positive public attention helping a nonprofit organization like us. Being a type [NAME] company makes you an ideal partner for us.</p>
    <p>Enclosed is a sponsorship proposal for your review. Please do not hesitate to contact us should you decide to become one of our sponsors. We will contact you in a few weeks to follow up on your decision and to answer any other queries and questions you may have regarding the sponsorship proposal and our organization.</p>
    <p>Thank you for taking time to review our proposal. We hope to hear from you soon.</p>
    <p>Regards,</p>
    <p class="signature">[YOUR SIGNATURE]</p>
    <p>[YOUR NAME]</p>
  </main>

  <div class="social">
    <span class="social-dot"></span>
    <span class="social-dot"></span>
    <span class="social-dot"></span>
    <span class="social-handle">@pelominis</span>
  </div>

  <svg class="bottom-bands" viewBox="0 0 849 90" aria-hidden="true">
    <polygon points="420,58 849,14 849,17 420,61" fill="var(--red)"/>
    <polygon points="440,90 849,30 849,90" fill="var(--blue)"/>
  </svg>
  <div class="web-address">www.pelo-minis.ch</div>
</div>
</body>
</html>
```